Quillmark Solutions - Website for a CRM IT Services Provider to Non-profits

We need a website design for our company that provides IT services to non-profits to enable them to manage their donors and philanthropy within their organization.

We would like to see a design that uses the colors in our logo and a funky take on how to uniquely present a topic as boring as IT. Examples of sites that we really like: brantwickdale.com, www.marlowpetrie.com, tinwhistlebox.com

The final design should communicate that we are a professional, yet creative company that is fun to work with.

Target Market(s)

Non-profits who tend to be young, creative types that are low-tech

Industry/Entity Type

It Company

Requirements
Must have
• Must include tabs for Home, Contact Us, About, Projects, and Blog. The site must use the logo we have attached on all of the page, in one way or another (it can be small & in the corner).

The site has to work on all mobile browsers (iphone, ipad).
Nice to have
• It would be great if I could supply some HTML for the Contact page that would allow me to capture leads and put them directly into my CRM application. It's very easy to set up.
Should not have
• The design should not use old-style fonts and should not have a lot of dark colors. Keep it similar to our logo, clean and simple. We're not looking for a busy home page.

```html
<!DOCTYPE html>
<html lang="en">
<head>
<meta charset="utf-8">
<title>Quillmark Solutions</title>
<link rel="stylesheet" href="https://fonts.googleapis.com/css2?family=Gelasio:wght@400&family=Arimo:wght@400&family=Roboto+Condensed:wght@400&display=swap">
<style>
  :root {
    --sky: #55d0e8;
    --white: #ffffff;
    --teal: #00b5a0;
    --teal-light: #16c2ad;
    --teal-dark: #009a88;
    --ink: #04222b;
    --field: #0b3c45;
    --lime: #9fba22;
    --text-grey: #4a4a4a;
    --footer-text: #16303a;
    --tile: #6d6d6d;
  }
  * { box-sizing: border-box; margin: 0; padding: 0; }
  html, body { width: 1200px; height: 1135px; overflow: hidden; }
  body {
    position: relative;
    background: var(--sky);
    font-family: "Arimo", Arial, sans-serif;
    color: var(--white);
  }
  .brand { position: absolute; left: 150px; top: 9px; width: 190px; text-align: center; }
  .brand-disc { width: 118px; height: 118px; border-radius: 50%; background: var(--white); margin: 0 auto; }
  .brand-name {
    margin-top: 14px;
    font-family: "Gelasio", Georgia, serif;
    font-size: 22px;
    color: var(--white);
    white-space: nowrap;
  }
  .main-nav {
    position: absolute; left: 524px; top: 89px; width: 539px; height: 31px;
    background: rgba(255,255,255,.16); border-radius: 4px;
    display: flex; justify-content: center; align-items: center; gap: 14px;
    font-family: "Gelasio", Georgia, serif; font-size: 19px;
  }
  .main-nav a { color: var(--white); text-decoration: none; }
  .star-badge { position: absolute; top: 238px; width: 54px; height: 56px; }
  .star-left { left: 140px; }
  .star-right { left: 1010px; }
  .tagline {
    position: absolute; left: 223px; top: 227px; width: 785px;
    font-family: "Gelasio", Georgia, serif; font-size: 20.5px; line-height: 31px;
  }
  .dash-frame {
    position: absolute; left: 141px; width: 918px;
    border: 2px dashed var(--white);
  }
  .showcase-frame { top: 346px; height: 338px; }
  .showcase {
    position: absolute; left: 152px; top: 357px; width: 896px; height: 316px;
    background: var(--teal);
  }
  .showcase-art {
    position: absolute; inset: 0;
    background:
      radial-gradient(ellipse 22% 38% at 30% 62%, rgba(4,34,43,.28), transparent 70%),
      radial-gradient(ellipse 14% 34% at 65% 38%, rgba(4,34,43,.26), transparent 70%),
      radial-gradient(ellipse 12% 22% at 18% 28%, rgba(4,34,43,.2), transparent 70%),
      radial-gradient(ellipse 18% 20% at 88% 48%, rgba(4,34,43,.16), transparent 70%),
      radial-gradient(ellipse 20% 14% at 52% 88%, rgba(255,255,255,.18), transparent 70%),
      linear-gradient(135deg, var(--teal-light), var(--teal) 50%, var(--teal-dark));
  }
  .slide-arrow { position: absolute; top: 148px; width: 46px; height: 40px; }
  .slide-prev { left: 2px; }
  .slide-next { right: 2px; }
  .about-frame { top: 711px; height: 178px; }
  .about-panel {
    position: absolute; left: 148px; top: 718px; width: 906px; height: 165px;
    background: var(--white);
  }
  .about-badge {
    position: absolute; left: 154px; top: 735px; width: 134px; height: 134px;
    border-radius: 50%; background: var(--lime);
    border: 4px solid #f2f2ea; box-shadow: 0 0 0 1px #cfcfc4, 0 2px 4px rgba(0,0,0,.25);
    display: flex; align-items: center; justify-content: center;
    font-family: "Roboto Condensed", Arial, sans-serif; font-size: 21px; color: var(--white);
  }
  .about-text {
    position: absolute; left: 307px; top: 763px; width: 730px;
    font-family: "Gelasio", Georgia, serif; font-size: 18px; line-height: 31px;
    color: var(--text-grey);
  }
  .feature {
    position: absolute; top: 911px; height: 149px; background: var(--ink);
    padding: 10px 18px 0 12px;
  }
  .feature h2 {
    font-family: "Gelasio", Georgia, serif; font-weight: 400; font-size: 24px; line-height: 28px;
    margin-bottom: 9px;
  }
  .feature p { font-size: 12px; line-height: 19px; margin-bottom: 11px; }
  .newsletter { left: 141px; width: 299px; border: 3px solid var(--white); padding: 7px 8px 0 9px; }
  .health { left: 450px; width: 300px; }
  .roi { left: 759px; width: 300px; padding-right: 14px; }
  .signup { position: absolute; left: 9px; top: 98px; width: 236px; height: 30px; background: var(--field); border-radius: 3px; }
  .signup-go { position: absolute; left: 258px; top: 103px; width: 20px; height: 20px; }
  .legal { position: absolute; left: 141px; top: 1079px; font-size: 13px; color: var(--footer-text); }
  .social { position: absolute; top: 1078px; width: 45px; height: 45px; border-radius: 4px; background: var(--tile); box-shadow: 0 1px 2px rgba(0,0,0,.4); }
  .social-one { left: 961px; }
  .social-two { left: 1014px; }
</style>
</head>
<body>
  <header>
    <div class="brand">
      <div class="brand-disc"></div>
      <div class="brand-name">Quillmark Solutions</div>
    </div>
    <nav class="main-nav">
      <a href="#">Home</a><span>/</span>
      <a href="#">Contact Us</a><span>/</span>
      <a href="#">About</a><span>/</span>
      <a href="#">Projects</a><span>/</span>
      <a href="#">Blog</a>
    </nav>
  </header>

  <svg class="star-badge star-left" viewBox="0 0 54 56" aria-hidden="true">
    <circle cx="27" cy="29" r="26" fill="#111"/>
    <circle cx="27" cy="27" r="24" fill="#fff" stroke="#111" stroke-width="2"/>
    <circle cx="27" cy="27" r="19" fill="none" stroke="#55d0e8" stroke-width="1.5"/>
    <polygon points="27,12 31,23 42,23 33,30 36,41 27,34 18,41 21,30 12,23 23,23" fill="#55d0e8" stroke="#111" stroke-width="2" stroke-linejoin="round"/>
  </svg>
  <p class="tagline">We provide consulting services for the Cloudfield.com platform, including full lifecycle implementations, health checks, business process mapping, and ROI analysis.</p>
  <svg class="star-badge star-right" viewBox="0 0 54 56" aria-hidden="true">
    <circle cx="27" cy="29" r="26" fill="#111"/>
    <circle cx="27" cy="27" r="24" fill="#fff" stroke="#111" stroke-width="2"/>
    <circle cx="27" cy="27" r="19" fill="none" stroke="#55d0e8" stroke-width="1.5"/>
    <polygon points="27,12 31,23 42,23 33,30 36,41 27,34 18,41 21,30 12,23 23,23" fill="#55d0e8" stroke="#111" stroke-width="2" stroke-linejoin="round"/>
  </svg>

  <div class="dash-frame showcase-frame"></div>
  <section class="showcase">
    <div class="showcase-art" role="img" aria-label="Flat illustration of devices and icons: a globe tablet, phones, a monitor with an eye, a tablet with a map pin, a pointing hand, pencils and a suspension bridge"></div>
    <svg class="slide-arrow slide-prev" viewBox="0 0 46 40" aria-hidden="true">
      <path d="M22 6 L8 20 L22 34 M9 20 H44" fill="none" stroke="#f2f2f2" stroke-width="5" stroke-linecap="round" stroke-linejoin="round"/>
    </svg>
    <svg class="slide-arrow slide-next" viewBox="0 0 46 40" aria-hidden="true">
      <path d="M24 6 L38 20 L24 34 M37 20 H2" fill="none" stroke="#f2f2f2" stroke-width="5" stroke-linecap="round" stroke-linejoin="round"/>
    </svg>
  </section>

  <div class="dash-frame about-frame"></div>
  <section class="about-panel"></section>
  <div class="about-badge">About us</div>
  <p class="about-text">We provide consulting services for the Cloudfield.com platform, including full lifecycle implementations, health checks, business process mapping, and ROI analysis.</p>

  <section class="feature newsletter">
    <h2>Newsletter</h2>
    <p>Be the first to hear when we release new designs, launch competitions and much more.</p>
    <div class="signup"></div>
    <svg class="signup-go" viewBox="0 0 20 20" aria-hidden="true">
      <circle cx="10" cy="10" r="9" fill="#fff"/>
      <circle cx="10" cy="10" r="7" fill="none" stroke="#04222b" stroke-width="1.5"/>
      <polygon points="8,6 14,10 8,14" fill="#04222b"/>
    </svg>
  </section>
  <section class="feature health">
    <h2>Health Checks</h2>
    <p>Includes a wide range of physiological tests with up to 45 minutes consultation with a Meridale doctor.</p>
    <p>Includes a wide range of physiological tests with up...</p>
  </section>
  <section class="feature roi">
    <h2>ROI Analysis</h2>
    <p>Return on Investment (ROI) analysis is one of several commonly used financial metrics for evaluating the financial consequences of business investments, decisions, or actions.</p>
  </section>

  <footer>
    <p class="legal">© 2012 Quillmark Inc.All Rights Reserved</p>
    <a class="social social-one" href="#" aria-label="Social profile"></a>
    <a class="social social-two" href="#" aria-label="Social profile"></a>
  </footer>
</body>
</html>
```